Postcard design for electronic tech toy at Marlow Play Expo

We are tech startup selling a new type of electric building block for kids. Compatible with MIBUs. This is a postcard to hand out at a trade show to remember the product with a website address on the back.

Quillmora is tech startup looking to get interest in our product, a electronic building block set compatible with MIBU bricks. We are looking for a smart, clean, professional look that compares with MIBU and moonTiles.

Target Market(s)

Education tech

Industry/Entity Type

Tech

Font styles to use
Serif
Sans Serif

```html
<!DOCTYPE html>
<html lang="en">
<head>
<meta charset="utf-8">
<title>Quillmora Postcard</title>
<link href="https://fonts.googleapis.com/css2?family=Montserrat:wght@600;700;800&family=Arimo:wght@400;700&display=swap" rel="stylesheet">
<style>
  :root{
    --stage:#474747;
    --red:#d8262b;
    --blue:#3aa7dc;
    --paper:#f1f1f1;
    --ink:#333333;
    --white:#ffffff;
    --kit-light:#ececec;
    --kit-mid:#cfcfcf;
  }
  *{box-sizing:border-box;margin:0;padding:0}
  html,body{width:1200px;height:1200px;overflow:hidden;background:var(--stage)}
  body{position:relative;font-family:"Arimo",Arial,sans-serif;color:var(--white)}
  .card{position:absolute;left:261px;width:739px;height:535px;background:var(--paper);overflow:hidden;box-shadow:0 6px 18px rgba(0,0,0,.45)}
  .card--front{top:54px}
  .card--back{top:622px}
  .layer{position:absolute;inset:0;width:100%;height:100%}
  .abs{position:absolute}

  .photo-kid{left:430px;top:0;width:309px;height:404px;background:linear-gradient(160deg,#c99a88 0%,#a56d68 40%,#6e4c55 75%,#4a3c40 100%)}
  .product{border-radius:14px;background:linear-gradient(160deg,var(--kit-light) 0%,var(--kit-mid) 100%);box-shadow:0 4px 10px rgba(0,0,0,.18)}
  .product--front{left:480px;top:262px;width:230px;height:128px}
  .product--back{left:350px;top:172px;width:345px;height:250px}

  .brand{font-family:"Montserrat",sans-serif;font-weight:700;font-size:29px;letter-spacing:1px;line-height:1}
  .tagline{font-family:"Montserrat",sans-serif;font-weight:600;font-size:10.5px;letter-spacing:2.6px;margin-top:8px}
  .brand-block--front{left:42px;top:76px;color:var(--white)}
  .brand-block--back{left:29px;top:76px}
  .brand-block--back .brand{color:var(--blue)}
  .brand-block--back .tagline{color:#555}

  .headline{font-family:"Montserrat",sans-serif;font-weight:800;line-height:1}
  .headline--big{left:40px;top:162px;font-size:56px}
  .headline--sub{left:41px;top:222px;font-size:31px}
  .lead{left:41px;top:278px;width:355px;font-size:19px;font-weight:700;line-height:24px}

  .info-band{left:0;top:404px;width:739px;height:68px;background:var(--white)}
  .info{left:41px;top:426px;display:flex;align-items:center;gap:12px;color:var(--ink)}
  .info__label{font-size:20px}
  .info__num{font-size:25px;font-weight:700;margin-left:4px}
  .url-band{left:0;top:472px;width:739px;height:63px;background:var(--blue);display:flex;align-items:center;justify-content:center}
  .url-band__text{font-size:21px;letter-spacing:8px;font-weight:700}

  .fun-title{left:350px;top:57px;font-size:34px}
  .fun-copy{left:350px;top:102px;width:370px;font-size:14px;line-height:17px}
  .how-title{left:30px;top:176px;font-family:"Montserrat",sans-serif;font-weight:700;font-size:27px;line-height:1}
  .how-sub{left:30px;top:215px;width:260px;font-size:14px;font-weight:700;line-height:17px}
  .steps{left:30px;top:266px;width:300px;list-style:none}
  .step{position:relative;padding-left:34px;height:73px}
  .step__tick{position:absolute;left:0;top:2px}
  .step__title{font-size:17px;font-weight:700}
  .step__text{font-size:12px;line-height:15px;margin-top:6px;width:255px}
  .social{left:451px;top:452px;display:flex;align-items:center;gap:9px;font-size:14px}
  .social__label{margin-right:8px}
  .social__dot{width:24px;height:24px;border-radius:50%;background:var(--white)}
  .contact-band{left:0;top:478px;width:739px;height:57px;background:var(--blue)}
  .contact{top:0;height:57px;display:flex;align-items:center;gap:12px;font-size:21px;font-weight:700}
  .contact--phone{left:33px}
  .contact--web{left:453px}
  .contact-divider{left:340px;top:9px;width:2px;height:40px;background:var(--white)}
</style>
</head>
<body>

<section class="card card--front">
  <div class="abs photo-kid" role="img" aria-label="Photo of a smiling girl building with electronic bricks"></div>
  <svg class="layer" viewBox="0 0 739 535" aria-hidden="true">
    <path d="M0 30 H366 C426 30 446 80 451 140 L466 260 C474 310 496 326 536 326 H739 V404 H0 Z" fill="var(--blue)"/>
    <path d="M0 30 H360 C420 30 440 80 445 140 L460 260 C468 310 490 326 530 326 H739 V404 H0 Z" fill="var(--red)"/>
  </svg>
  <div class="abs info-band"></div>
  <div class="abs url-band"><span class="url-band__text">www.quillmora.com</span></div>
  <div class="abs product product--front" role="img" aria-label="Photo of the electronic brick kit with wires and lights"></div>

  <div class="abs brand-block--front">
    <div class="brand">QUILLMORA</div>
    <div class="tagline">POWER UP YOUR IMAGINATION</div>
  </div>
  <h1 class="abs headline headline--big">GIVE YOUR</h1>
  <h2 class="abs headline headline--sub">BRICKS BRAINS!</h2>
  <p class="abs lead">Quillmora™ is a unique building kit where kids can learn how to build digital circuits.</p>

  <div class="abs info">
    <span class="info__label">For more info</span>
    <svg width="24" height="26" viewBox="0 0 24 24" aria-hidden="true"><path d="M6.6 2.5c.8-.5 1.7-.2 2.1.6l1.8 3.4c.4.7.2 1.6-.4 2.1l-1.5 1.2c1 2.4 2.8 4.4 5 5.7l1.3-1.4c.6-.6 1.5-.7 2.2-.3l3.3 2c.7.5 1 1.4.5 2.2l-1.3 2.1c-.6 1-1.8 1.5-2.9 1.2C9.7 19.6 4 13.5 2.6 6.4c-.2-1.100.3-2.2 1.3-2.8z" fill="var(--red)"/></svg>
    <span class="info__num">+123 - 456 - 7890</span>
  </div>
</section>

<section class="card card--back">
  <svg class="layer" viewBox="0 0 739 535" aria-hidden="true">
    <path d="M0 147 H244 C284 147 294 134 306 104 L324 59 C336 32 354 24 394 24 H739 V478 H0 Z" fill="var(--blue)"/>
    <path d="M0 153 H250 C290 153 300 140 312 110 L330 65 C342 38 360 30 400 30 H739 V478 H0 Z" fill="var(--red)"/>
  </svg>
  <div class="abs product product--back" role="img" aria-label="Photo of the electronic brick kit with wires and lights"></div>

  <div class="abs brand-block--back">
    <div class="brand">QUILLMORA</div>
    <div class="tagline">POWER UP YOUR IMAGINATION</div>
  </div>

  <h2 class="abs headline fun-title">AND, HAVE FUN!</h2>
  <p class="abs fun-copy">Build from our examples to learn about digital electronics, explore your new world. Then, as we say: Power Up your Imagination</p>

  <h3 class="abs how-title">HOW IT WORKS</h3>
  <p class="abs how-sub">Quillmora makes building digital electronics a SNAP</p>

  <ol class="abs steps">
    <li class="step">
      <svg class="step__tick" width="20" height="20" viewBox="0 0 20 20" aria-hidden="true"><circle cx="9" cy="11" r="8" fill="none" stroke="var(--blue)" stroke-width="2"/><path d="M5 10.5l4 4 9-10" fill="none" stroke="var(--blue)" stroke-width="2.4" stroke-linecap="round"/></svg>
      <div class="step__title">1. Power your hub</div>
      <p class="step__text">Snap together any number of hub bricks from your power brick.</p>
    </li>
    <li class="step">
      <svg class="step__tick" width="20" height="20" viewBox="0 0 20 20" aria-hidden="true"><circle cx="9" cy="11" r="8" fill="none" stroke="var(--blue)" stroke-width="2"/><path d="M5 10.5l4 4 9-10" fill="none" stroke="var(--blue)" stroke-width="2.4" stroke-linecap="round"/></svg>
      <div class="step__title">2. Add some logic</div>
      <p class="step__text">Click in your logic, buttons, and knobs in the center rows of the hub</p>
    </li>
    <li class="step">
      <svg class="step__tick" width="20" height="20" viewBox="0 0 20 20" aria-hidden="true"><circle cx="9" cy="11" r="8" fill="none" stroke="var(--blue)" stroke-width="2"/><path d="M5 10.5l4 4 9-10" fill="none" stroke="var(--blue)" stroke-width="2.4" stroke-linecap="round"/></svg>
      <div class="step__title">3. Wire it up</div>
      <p class="step__text">Wire up the edges to connect the bricks together. Watch the lights start to flash!</p>
    </li>
  </ol>

  <div class="abs social">
    <span class="social__label">Get connected with us</span>
    <span class="social__dot"></span>
    <span class="social__dot"></span>
    <span class="social__dot"></span>
  </div>

  <div class="abs contact-band">
    <div class="abs contact contact--phone">
      <svg width="20" height="20" viewBox="0 0 24 24" aria-hidden="true"><path d="M6.6 2.5c.8-.5 1.7-.2 2.1.6l1.8 3.4c.4.7.2 1.6-.4 2.1l-1.5 1.2c1 2.4 2.8 4.4 5 5.7l1.3-1.4c.6-.6 1.5-.7 2.2-.3l3.3 2c.7.5 1 1.4.5 2.2l-1.3 2.1c-.6 1-1.8 1.5-2.9 1.2C9.7 19.6 4 13.5 2.6 6.4c-.2-1.1.3-2.2 1.3-2.8z" fill="var(--white)"/></svg>
      <span>123 - 456 - 7890</span>
    </div>
    <div class="abs contact-divider"></div>
    <div class="abs contact contact--web">
      <svg width="20" height="20" viewBox="0 0 24 24" aria-hidden="true"><g fill="none" stroke="var(--white)" stroke-width="2"><circle cx="12" cy="12" r="10"/><ellipse cx="12" cy="12" rx="4.5" ry="10"/><path d="M2 12h20M4 6.5h16M4 17.5h16"/></g></svg>
      <span>www.quillmora.com</span>
    </div>
  </div>
</section>

</body>
</html>
```